One Page Sales Flyer for Wireless Survey- Computer Hardware

I want a designer to create a one page 4 color sales slick to be given to our sales team to sell to the end customers. I would like a visual picture of a heat map so zavvix "heat map wireless" to get an idea of how that image should look.

```html
<!DOCTYPE html>
<html lang="en">
<head>
<meta charset="utf-8">
<title>Corvane – Wireless Site Surveys Flyer</title>
<link href="https://fonts.googleapis.com/css2?family=Roboto+Condensed:wght@400;700&family=Lato:wght@400;700&display=swap" rel="stylesheet">
<style>
  :root{
    --page-bg:#ece7e1;
    --white:#ffffff;
    --brand-blue:#3a9edb;
    --deep-blue:#1f5c9a;
    --ink:#333333;
    --body-ink:#444444;
    --panel-grey:#7d7d7d;
    --map-fill:#d8e3a8;
  }
  *{box-sizing:border-box;margin:0;padding:0}
  html,body{width:1200px;height:1200px;overflow:hidden;background:var(--page-bg)}
  body{position:relative;font-family:'Lato',sans-serif;color:var(--body-ink)}

  .flyer{position:absolute;left:175px;top:20px;width:850px;height:1160px;background:var(--white);overflow:hidden;box-shadow:0 2px 10px rgba(0,0,0,.12)}

  .masthead{height:122px;display:flex;align-items:center;justify-content:space-between;padding:0 40px 0 42px}
  .brand{display:flex;align-items:center;gap:16px}
  .brand-mark{width:76px;height:76px;border-radius:10px;background:var(--brand-blue)}
  .brand-name{font-family:'Roboto Condensed',sans-serif;font-weight:400;font-size:40px;letter-spacing:2px;color:var(--ink)}
  .headline{text-align:right;font-family:'Roboto Condensed',sans-serif}
  .headline-kicker{font-size:25px;color:var(--ink);line-height:1.1}
  .headline-main{font-size:38px;color:var(--brand-blue);line-height:1.15}

  .heat-map{height:330px;background:var(--map-fill)}
  .accent-rule{height:10px;background:var(--brand-blue)}

  .content{position:relative;height:628px}
  .info{position:absolute;left:38px;top:24px;width:445px}
  .info h2{font-family:'Roboto Condensed',sans-serif;font-weight:400;font-size:18px;color:var(--brand-blue);display:inline-block;border-bottom:1px solid var(--brand-blue);padding-bottom:3px;margin-bottom:18px}
  .info p{font-size:14px;line-height:20px;text-align:justify;margin-bottom:24px}
  .info ul{list-style:none;font-size:14px;line-height:20px}
  .info li{position:relative;padding-left:24px;text-align:justify}
  .info li::before{content:"";position:absolute;left:2px;top:8px;width:5px;height:5px;border-radius:50%;background:var(--ink)}

  .targets{position:absolute;left:508px;top:24px;right:0}
  .targets h2{font-family:'Roboto Condensed',sans-serif;font-weight:400;font-size:18px;color:var(--brand-blue);display:inline-block;border-bottom:2px solid var(--brand-blue);padding-bottom:3px;margin-left:10px}
  .target-panel{margin-top:18px;margin-left:6px;height:552px;background:var(--panel-grey);padding-top:14px}
  .target-list{list-style:none}
  .target{position:relative;height:54px;display:flex;align-items:center;padding-left:42px;font-family:'Roboto Condensed',sans-serif;font-weight:700;font-size:22px;color:var(--white)}
  .target-icon{position:absolute;left:-24px;top:6px;width:42px;height:42px;border-radius:50%;background:var(--deep-blue);border:2px solid var(--white);display:flex;align-items:center;justify-content:center}
  .target-icon svg{width:22px;height:22px;fill:none;stroke:var(--white);stroke-width:2}

  .contact-bar{position:absolute;left:0;right:0;bottom:0;height:70px;background:var(--brand-blue);display:flex;align-items:center;padding:0 40px 0 64px;color:var(--white);font-weight:700;font-size:15px}
  .contact-title{font-family:'Roboto Condensed',sans-serif;font-size:24px;margin-right:60px}
  .contact-item{display:flex;align-items:center;gap:8px;margin-right:34px}
  .contact-item:last-child{margin-right:0}
  .contact-item svg{width:20px;height:20px;fill:none;stroke:var(--white);stroke-width:1.8}
</style>
</head>
<body>
<main class="flyer">
  <header class="masthead">
    <div class="brand">
      <div class="brand-mark"></div>
      <span class="brand-name">CORVANE</span>
    </div>
    <div class="headline">
      <div class="headline-kicker">Increase Hardware and Services Spend</div>
      <div class="headline-main">With Wireless Site Surveys</div>
    </div>
  </header>

  <div class="heat-map" role="img" aria-label="Wireless signal heat map over a street map around a pinned office address"></div>
  <div class="accent-rule"></div>

  <section class="content">
    <div class="info">
      <h2>What is a wireless site survey or heat map?</h2>
      <p>A wireless site survey is a compilation of reports showing a visual representation of health of your wireless network. This does not only show how strong or weak a wireless signal is in any location it also helps aid in channel and placement to ensure maximum stable data rates are archived even where the single appears strong.</p>
      <h2>Why do customers need a site survey?</h2>
      <p>Any variety of factors can contribute to an unhealthy wireless network (electrical, motors, materials used in construction, distance, neighboring wireless networks, etc.) and traditional methods that use only blueprints and a computer program to show signal strength have shown to be ineffective.</p>
      <h2>Why should they use you?</h2>
      <ul>
        <li>42% of businesses report some issues with wireless connectivity and acknowledge its effect on the bottom line*.</li>
        <li>Most of these problems are solved through either fine tuning the current equipment (managed services) or purchasing new equipment (incremental sales) of which you can provide both.</li>
        <li>Being a one-stop shop for all your customer's IT needs prevents them from needing additional vendors.</li>
        <li>The increase of IoT (Internet of things) and BYOD (Bring Your Own Device).</li>
      </ul>
    </div>

    <aside class="targets">
      <h2>TARGET CUSTOMERS</h2>
      <div class="target-panel">
        <ul class="target-list">
          <li class="target"><span class="target-icon"><svg viewBox="0 0 24 24"><circle cx="8" cy="5" r="2"/><circle cx="16" cy="5" r="2"/><path d="M8 8v12M16 8v12M5 12h14"/></svg></span>DISTRIBUTORS</li>
          <li class="target"><span class="target-icon"><svg viewBox="0 0 24 24"><path d="M3 11l9-6 9 6v9H3z"/><path d="M8 20v-6h8v6"/></svg></span>WAREHOUSES</li>
          <li class="target"><span class="target-icon"><svg viewBox="0 0 24 24"><path d="M4 20h16M6 20V10h12v10M12 4v6M12 4l5 2-5 2"/></svg></span>SLED</li>
          <li class="target"><span class="target-icon"><svg viewBox="0 0 24 24"><rect x="4" y="5" width="16" height="10"/><path d="M7 15v5M17 15v5"/></svg></span>K-12</li>
          <li class="target"><span class="target-icon"><svg viewBox="0 0 24 24"><path d="M12 19s-7-4.5-7-9a4 4 0 017-2.5A4 4 0 0119 10c0 4.5-7 9-7 9z"/></svg></span>MEDICAL / HOSPITALS</li>
          <li class="target"><span class="target-icon"><svg viewBox="0 0 24 24"><rect x="5" y="4" width="14" height="16"/><path d="M9 8h2M13 8h2M9 12h2M13 12h2M11 20v-4h2v4"/></svg></span>ENTERPRISE F1000</li>
          <li class="target"><span class="target-icon"><svg viewBox="0 0 24 24"><circle cx="12" cy="12" r="8"/><path d="M4 12h16M12 4v16"/></svg></span>SPORTS VENUES</li>
          <li class="target"><span class="target-icon"><svg viewBox="0 0 24 24"><ellipse cx="12" cy="9" rx="8" ry="3"/><path d="M4 9v7c0 1.7 3.6 3 8 3s8-1.3 8-3V9"/></svg></span>STADIUMS</li>
          <li class="target"><span class="target-icon"><svg viewBox="0 0 24 24"><rect x="4" y="4" width="16" height="16"/><path d="M4 9h16M8 13h2M14 13h2M8 16h2M14 16h2"/></svg></span>HOTELS</li>
          <li class="target"><span class="target-icon"><svg viewBox="0 0 24 24"><path d="M3 5h3l2 10h11l2-7H7"/><circle cx="9" cy="19" r="1.5"/><circle cx="17" cy="19" r="1.5"/></svg></span>RETAIL STORES</li>
        </ul>
      </div>
    </aside>
  </section>

  <footer class="contact-bar">
    <span class="contact-title">Contact US</span>
    <span class="contact-item"><svg viewBox="0 0 24 24"><path d="M5 4h4l2 5-2.5 1.5a11 11 0 005 5L15 13l5 2v4a2 2 0 01-2 2A16 16 0 013 6a2 2 0 012-2z"/></svg>555-014-2290</span>
    <span class="contact-item"><svg viewBox="0 0 24 24"><circle cx="12" cy="12" r="9"/><path d="M3 12h18M12 3c3 3 3 15 0 18M12 3c-3 3-3 15 0 18"/></svg>www.corvanetech.com</span>
    <span class="contact-item"><svg viewBox="0 0 24 24"><rect x="3" y="5" width="18" height="14"/><path d="M3 5l9 8 9-8"/></svg>info@corvanetech.com</span>
  </footer>
</main>
</body>
</html>
```